Borvelux Bootcamp Schedule

Nothing complicated just a basic (but well designed) bootcamp schedule in the form of a flyer to hand out.

Explanation below:

We hand out our fitness bootcamp schedule to potential clients and members on a regular basis and want to make a good impression about who we are and the detail we put into our material and services. I've attached a current schedule that we send out. I'm hoping we can get this as a PSD file so we can change the times and days as needed as our company grows. I've also attached a jpeg of our new website design and what that will look like along with our Borvelux Personal Training Studio logo and our Borvelux Bootcamps logo. The schedule is for our bootcamp. I also included several photos of our facility and if you want pictures of anything up close or anything that you would want in the design I can snap a good photo and send it. I included an attempt of my own to make a schedule that I wasn't too fond of but tried :)

Industry/Entity Type

Fitness

```html
<!DOCTYPE html>
<html lang="en">
<head>
<meta charset="utf-8">
<title>Borvelux Bootcamps – Training Schedule</title>
<link rel="stylesheet" href="https://fonts.googleapis.com/css2?family=Archivo+Black&family=Sansita:wght@800&family=Varela+Round&family=Comic+Neue:ital,wght@1,700&display=swap">
<style>
  :root {
    --ink: #000000;
    --night: #050505;
    --signal-red: #e3151b;
    --deep-red: #a90d10;
    --steel: #8d8d8d;
    --steel-light: #d6d3d3;
    --parchment: #cdb48d;
    --parchment-dark: #8e6a40;
    --wood: #4a3120;
    --skin: #a8644a;
    --hair: #1a0f0c;
    --logo-panel: #f2f2f2;
    --logo-ink: #2f6fae;
  }
  * { margin: 0; padding: 0; box-sizing: border-box; }
  html, body { width: 848px; height: 1200px; overflow: hidden; background: var(--night); }

  .flyer { position: relative; width: 848px; height: 1200px; background: var(--night); overflow: hidden; }

  .top-band { position: absolute; left: 0; top: 0; width: 848px; height: 120px; }

  .brand-plate {
    position: absolute; left: 158px; top: 11px; width: 530px; height: 82px;
    background: var(--logo-panel); border: 3px solid var(--ink);
    display: flex; align-items: center; justify-content: center; gap: 14px;
  }
  .brand-mark { width: 18px; height: 18px; background: var(--logo-ink); flex: none; }
  .brand-name {
    font-family: "Archivo Black", sans-serif; font-size: 31px; letter-spacing: 1px;
    color: var(--logo-ink); text-transform: uppercase; white-space: nowrap;
  }

  .parchment-art {
    position: absolute; left: 22px; top: 165px; width: 500px; height: 818px;
    transform: rotate(-1.5deg);
    background: radial-gradient(ellipse at 50% 45%, var(--parchment) 55%, var(--parchment-dark) 88%, var(--wood) 100%);
    border: 8px solid var(--wood);
  }

  .athlete-photo {
    position: absolute; left: 522px; top: 420px; width: 326px; height: 682px;
    background: radial-gradient(ellipse at 50% 30%, var(--skin) 0%, #6d3b2b 35%, var(--hair) 70%, var(--night) 100%);
  }

  .schedule {
    position: absolute; left: 50px; top: 340px; width: 470px;
    transform: rotate(-6deg); transform-origin: 0 0; text-align: center;
  }
  .schedule-title {
    font-family: "Sansita", sans-serif; font-weight: 800; font-size: 34px; letter-spacing: 3px;
    color: var(--signal-red); -webkit-text-stroke: 1px var(--ink); text-transform: uppercase;
    text-align: left; white-space: nowrap;
  }
  .schedule-day {
    font-family: "Sansita", sans-serif; font-weight: 800; font-size: 30px; letter-spacing: 1px;
    color: var(--signal-red); -webkit-text-stroke: 1px var(--ink);
  }
  .day-weekdays { margin-top: 58px; margin-left: 40px; }
  .day-saturday { margin-top: 40px; margin-left: 30px; text-transform: uppercase; }
  .time-list { list-style: none; margin-top: 46px; }
  .time-list li {
    font-family: "Varela Round", sans-serif; font-size: 26px; letter-spacing: 3px;
    color: var(--ink); line-height: 27px; white-space: nowrap;
  }
  .time-saturday { margin-top: 38px; }
  .schedule-note {
    margin-top: 40px; font-family: "Comic Neue", cursive; font-style: italic; font-weight: 700;
    font-size: 18px; line-height: 24px; color: var(--ink); padding-left: 90px; text-align: left;
    white-space: nowrap;
  }

  .headline-badge { position: absolute; left: 424px; top: 220px; width: 424px; height: 250px; }
  .headline {
    position: absolute; left: 424px; top: 281px; width: 424px; text-align: center;
    font-family: "Archivo Black", sans-serif; font-size: 35px; line-height: 41px; letter-spacing: 1px;
    color: var(--ink); white-space: nowrap;
  }

  .bottom-band {
    position: absolute; left: 0; top: 1102px; width: 848px; height: 98px;
    background: linear-gradient(var(--signal-red), var(--deep-red));
    border-top: 4px solid var(--steel);
    padding: 18px 0 0 26px;
  }
  .contact-line {
    font-family: "Archivo Black", sans-serif; font-size: 25px; letter-spacing: 1.5px;
    color: var(--ink); line-height: 33px; white-space: nowrap;
  }
  .contact-dot { display: inline-block; width: 8px; height: 8px; background: var(--ink); border-radius: 50%; margin: 0 4px; vertical-align: middle; }
</style>
</head>
<body>
<main class="flyer">
  <svg class="top-band" viewBox="0 0 848 120" aria-hidden="true">
    <path d="M0 0 H848 V60 Q700 100 620 108 H230 Q150 100 0 60 Z" fill="var(--steel-light)"/>
    <path d="M0 0 H848 V50 Q700 90 620 96 H230 Q150 90 0 50 Z" fill="var(--signal-red)"/>
  </svg>

  <header class="brand-plate">
    <span class="brand-mark"></span>
    <span class="brand-name">Borvelux Bootcamps</span>
  </header>

  <div class="parchment-art" role="img" aria-label="Aged parchment scroll on a dark wooden board"></div>

  <div class="athlete-photo" role="img" aria-label="Photo of a fit woman in black sportswear holding dumbbells"></div>

  <section class="schedule">
    <h1 class="schedule-title">Training Schedule</h1>
    <h2 class="schedule-day day-weekdays">Monday-Friday</h2>
    <ul class="time-list">
      <li>6:00AM-7:00AM</li>
      <li>8:30AM-9:30AM</li>
      <li>12:00PM-1:00PM</li>
      <li>5:30PM-6:30PM</li>
      <li>6:30PM-7:30PM</li>
    </ul>
    <h2 class="schedule-day day-saturday">Saturday</h2>
    <ul class="time-list time-saturday">
      <li>9:00AM-10AM</li>
    </ul>
    <p class="schedule-note">Bootcamp times are subject to change<br>due to weather and holidays.</p>
  </section>

  <svg class="headline-badge" viewBox="0 0 440 250" preserveAspectRatio="none" aria-hidden="true">
    <polygon fill="var(--steel-light)" points="435,125 401.5,144 418.7,171 373.7,179.5 372,209.8 322.9,206.4 302.3,235.9 256,221.1 220,245 184,221.1 137.7,235.9 117.1,206.4 68,209.8 66.3,179.5 21.3,171 38.5,144 5,125 38.5,106 21.3,79 66.3,70.5 68,40.2 117.1,43.6 137.7,14.1 184,28.9 220,5 256,28.9 302.3,14.1 322.9,43.6 372,40.2 373.7,70.5 418.7,79 401.5,106"/>
    <polygon fill="var(--signal-red)" transform="translate(220 125) scale(0.93) translate(-220 -125)" points="435,125 401.5,144 418.7,171 373.7,179.5 372,209.8 322.9,206.4 302.3,235.9 256,221.1 220,245 184,221.1 137.7,235.9 117.1,206.4 68,209.8 66.3,179.5 21.3,171 38.5,144 5,125 38.5,106 21.3,79 66.3,70.5 68,40.2 117.1,43.6 137.7,14.1 184,28.9 220,5 256,28.9 302.3,14.1 322.9,43.6 372,40.2 373.7,70.5 418.7,79 401.5,106"/>
  </svg>
  <p class="headline">Total Body<br>Transformation<br>Workout</p>

  <footer class="bottom-band">
    <p class="contact-line">18 W.Cedar Ave. Fairhaven,CO 80000</p>
    <p class="contact-line">555-014-2876<span class="contact-dot"></span>www.borvelux.com</p>
  </footer>
</main>
</body>
</html>
```